Business Cards- The Manor at Brookridge Golf Club

We would like our business cards to look more high-end. We are a wedding venue that has been in business for 60+ years. We like our logo and our colors - primarily green and a touch of gold/beige. The owner wants our business cards to look more special..

Target Market(s)

Brides who have already toured our venue

Industry/Entity Type

Wedding venue - mansion

Contact Information for Business Card

Name, email, physical address, phone number

Colors
00AB8E
00BBA5
67D7C9
C6EFE9
E9F9F6

Requirements
Must have
• I think we would like our cards to be so pretty that people will want to keep them and will remember the venue. The venue is historic (built in 1850) and beautiful.
Nice to have
• Could we put an image of the building on one side and the contact info on the other?
Should not have
• The color black

```html
<!DOCTYPE html>
<html lang="en">
<head>
<meta charset="utf-8">
<title>The Manor at Brookridge Golf Club – Business Card</title>
<link rel="stylesheet" href="https://fonts.googleapis.com/css2?family=Montserrat:wght@400;500;600;700&display=swap">
<style>
  :root {
    --page-bg: #e9ece8;
    --card-white: #fbfbf9;
    --venue-green: #6a9a36;
    --venue-green-bright: #a9dc68;
    --gold-beige: #cdbd9d;
    --gold-light: #e3d8c2;
    --text-light: #ffffff;
    --sky-top: #3f7fd0;
    --sky-low: #9cc3ee;
    --tree-dark: #1f3b22;
    --lawn: #5c8f34;
  }
  * { box-sizing: border-box; margin: 0; padding: 0; }
  html, body { width: 1200px; height: 874px; overflow: hidden; }
  body {
    background: var(--page-bg);
    font-family: "Montserrat", sans-serif;
    position: relative;
  }
  .card {
    position: absolute;
    left: 290px;
    width: 620px;
    height: 354px;
    overflow: hidden;
    box-shadow: 0 10px 28px rgba(40, 50, 40, 0.22);
  }
  .card-front { top: 63px; }
  .card-back { top: 457px; background: var(--card-white); }

  .venue-photo {
    position: absolute; inset: 0;
    background:
      linear-gradient(180deg, transparent 0%, transparent 70%, var(--lawn) 78%, #6f9f44 100%),
      linear-gradient(180deg, transparent 0%, transparent 28%, var(--tree-dark) 40%, #2b4a2a 74%),
      linear-gradient(180deg, var(--sky-top) 0%, var(--sky-low) 40%);
  }
  .front-name {
    position: absolute;
    left: 210px; top: 128px;
    width: 360px;
    color: var(--venue-green-bright);
    font-weight: 600;
    font-size: 26px;
    line-height: 1.2;
    display: flex; align-items: center; gap: 12px;
  }
  .mark-square {
    flex: 0 0 auto;
    width: 14px; height: 14px;
    background: var(--gold-beige);
  }

  .back-wave { position: absolute; inset: 0; }
  .back-name {
    position: absolute;
    left: 38px; top: 58px;
    color: var(--venue-green);
    font-weight: 600;
    font-size: 24px;
    line-height: 1.2;
    width: 300px;
    display: flex; align-items: center; gap: 10px;
  }
  .contact {
    position: absolute;
    right: 34px; top: 194px;
    text-align: right;
    color: var(--text-light);
  }
  .contact-name {
    font-weight: 700;
    font-size: 18px;
    line-height: 1.2;
    letter-spacing: 1.5px;
    text-transform: uppercase;
  }
  .contact-title {
    font-size: 12px;
    letter-spacing: 1px;
    margin-top: 2px;
    margin-bottom: 9px;
  }
  .contact-line {
    font-size: 12.5px;
    letter-spacing: 0.5px;
    line-height: 1.45;
    display: flex; justify-content: flex-end; align-items: center; gap: 7px;
  }
  .contact-line svg { width: 11px; height: 11px; fill: var(--text-light); }
  .address { margin-bottom: 6px; }
</style>
</head>
<body>

  <section class="card card-front">
    <div class="venue-photo" role="img" aria-label="Photo of an outdoor wedding ceremony setup: rows of white chairs on a lawn facing a wooden arch, tall evergreen hedge and blue sky with clouds"></div>
    <div class="front-name"><span class="mark-square"></span><span>The Manor at Brookridge Golf Club</span></div>
  </section>

  <section class="card card-back">
    <svg class="back-wave" viewBox="0 0 620 354" preserveAspectRatio="none" aria-hidden="true">
      <path d="M0,128 C20,258 100,288 170,278 C260,268 340,108 620,78 L620,354 L0,354 Z" fill="var(--gold-light)"/>
      <path d="M0,134 C20,264 100,294 170,284 C260,274 340,114 620,84 L620,354 L0,354 Z" fill="var(--gold-beige)"/>
      <path d="M0,140 C20,270 100,300 170,290 C260,280 340,120 620,90 L620,354 L0,354 Z" fill="var(--venue-green)"/>
    </svg>

    <div class="back-name"><span class="mark-square"></span><span>The Manor at Brookridge Golf Club</span></div>

    <div class="contact">
      <p class="contact-name">Helena Whitford</p>
      <p class="contact-title">President - Owner</p>
      <p class="contact-line">2847 Larkspur Lane</p>
      <p class="contact-line address">Fairhaven, MD 21390</p>
      <p class="contact-line">(555) 310-4826
        <svg viewBox="0 0 24 24"><path d="M6.6 10.8a15.5 15.5 0 0 0 6.6 6.6l2.2-2.2c.3-.3.7-.4 1-.2 1.1.4 2.3.6 3.6.6.6 0 1 .4 1 1V20c0 .6-.4 1-1 1A17 17 0 0 1 3 4c0-.6.4-1 1-1h3.5c.6 0 1 .4 1 1 0 1.3.2 2.5.6 3.6.1.3 0 .7-.2 1z"/></svg>
      </p>
      <p class="contact-line">(555) 208-6619
        <svg viewBox="0 0 24 24"><path d="M7 1h10a2 2 0 0 1 2 2v18a2 2 0 0 1-2 2H7a2 2 0 0 1-2-2V3a2 2 0 0 1 2-2zm0 3v14h10V4zm5 15.5a1 1 0 1 0 0 2 1 1 0 0 0 0-2z"/></svg>
      </p>
      <p class="contact-line">hwhitford@brookridgegolfclub.com
        <svg viewBox="0 0 24 24"><path d="M2 5h20v14H2zm2 2v.5l8 5 8-5V7zm0 2.8V17h16V9.8l-8 5z"/></svg>
      </p>
    </div>
  </section>

</body>
</html>
```